IT services company needs a business card designed

-2 sided business card.-Front is going to be the logo raised (3D floating effect) on a black background. Make the logos spider web shiny silver and keep the spider the same design. -Back needs to have the following information:Darrel Sotho, Managing Partner, Cell: 738-402-1954, Website: Plankhorn.com, Email: Darrel@Plankhorn.com
Target Market(s)
IT Services
Industry/Entity Type
It Company
Contact Information for Business Card
-2 sided business card.
-Front is going to be the logo raised (3D floating effect) on a black background. Make the logos spider web shiny silver and keep the spider the same design.
-Back needs to have the following information:
Darrel Sotho, Managing Partner, Cell: 738-402-1954, Website: Plankhorn.com, Email: Darrel@Plankhorn.com

```html
<!DOCTYPE html>
<html lang="en">
<head>
<meta charset="utf-8">
<title>Plankhorn – Business Card Back</title>
<link rel="stylesheet" href="https://fonts.googleapis.com/css2?family=Saira+Semi+Condensed:wght@400;500&display=swap">
<style>
  :root {
    --sky-top: #34aef7;
    --sky-bottom: #1b7a9b;
    --accent-cyan: #00fbff;
    --ink-white: #ffffff;
  }
  html, body {
    margin: 0;
    padding: 0;
    overflow: hidden;
    background: #ffffff;
  }
  .card {
    position: relative;
    width: 1200px;
    height: 773px;
    overflow: hidden;
    background: linear-gradient(180deg, var(--sky-top) 0%, var(--sky-bottom) 100%);
    font-family: "Saira Semi Condensed", "Arial Narrow", sans-serif;
    color: var(--ink-white);
  }
  .strip-top {
    position: absolute;
    left: 561px;
    top: -40px;
    width: 80px;
    height: 114px;
    border-radius: 40px;
    background: var(--accent-cyan);
  }
  .strip-bottom {
    position: absolute;
    left: 561px;
    top: 437px;
    width: 80px;
    height: 400px;
    border-radius: 40px 40px 0 0;
    background: var(--accent-cyan);
  }
  .brand-name {
    position: absolute;
    left: 0;
    width: 1200px;
    top: 298px;
    margin: 0;
    text-align: center;
    font-size: 40px;
    font-weight: 500;
    letter-spacing: 1px;
    line-height: 1;
  }
  .holder {
    position: absolute;
    left: 107px;
    top: 551px;
  }
  .holder-name {
    margin: 0;
    font-size: 54px;
    font-weight: 500;
    line-height: 1;
    text-transform: uppercase;
    letter-spacing: 0.5px;
  }
  .holder-title {
    margin: 8px 0 0;
    font-size: 25px;
    font-weight: 400;
    line-height: 1;
  }
  .contact-list {
    position: absolute;
    left: 584px;
    top: 510px;
    margin: 0;
    padding: 0;
    list-style: none;
  }
  .contact-item {
    display: flex;
    align-items: center;
    height: 36px;
    margin-bottom: 35px;
  }
  .contact-icon {
    width: 34px;
    height: 36px;
    flex: none;
  }
  .contact-rule {
    width: 50px;
    height: 1.5px;
    background: var(--ink-white);
    margin: 0 12px 0 4px;
    flex: none;
  }
  .contact-text {
    font-size: 29px;
    font-weight: 400;
    white-space: nowrap;
  }
</style>
</head>
<body>
  <div class="card">
    <div class="strip-top"></div>
    <div class="strip-bottom"></div>

    <p class="brand-name">PLANKHORN</p>

    <div class="holder">
      <h1 class="holder-name">Darrel Sotho</h1>
      <p class="holder-title">Managing Partner</p>
    </div>

    <ul class="contact-list">
      <li class="contact-item">
        <svg class="contact-icon" viewBox="0 0 34 36" aria-hidden="true">
          <rect x="8" y="1" width="18" height="34" rx="2.5" fill="none" stroke="#fff" stroke-width="1.6"/>
          <line x1="8" y1="6" x2="26" y2="6" stroke="#fff" stroke-width="1.2"/>
          <line x1="8" y1="29" x2="26" y2="29" stroke="#fff" stroke-width="1.2"/>
          <line x1="15" y1="32" x2="19" y2="32" stroke="#fff" stroke-width="1.2"/>
        </svg>
        <span class="contact-rule"></span>
        <span class="contact-text">Cell: 738-402-1954,</span>
      </li>
      <li class="contact-item">
        <svg class="contact-icon" viewBox="0 0 34 36" aria-hidden="true">
          <circle cx="17" cy="18" r="15" fill="none" stroke="#fff" stroke-width="1.6"/>
          <ellipse cx="17" cy="18" rx="7" ry="15" fill="none" stroke="#fff" stroke-width="1.2"/>
          <line x1="2" y1="18" x2="32" y2="18" stroke="#fff" stroke-width="1.2"/>
          <line x1="5" y1="10" x2="29" y2="10" stroke="#fff" stroke-width="1.2"/>
          <line x1="5" y1="26" x2="29" y2="26" stroke="#fff" stroke-width="1.2"/>
        </svg>
        <span class="contact-rule"></span>
        <span class="contact-text">Website: Plankhorn.com,</span>
      </li>
      <li class="contact-item">
        <svg class="contact-icon" viewBox="0 0 34 36" aria-hidden="true">
          <g transform="rotate(-35 17 18)">
            <rect x="5" y="10" width="24" height="16" fill="none" stroke="#fff" stroke-width="1.6"/>
            <polyline points="5,10 17,20 29,10" fill="none" stroke="#fff" stroke-width="1.4"/>
          </g>
          <line x1="2" y1="30" x2="9" y2="23" stroke="#fff" stroke-width="1.2"/>
          <line x1="4" y1="34" x2="12" y2="26" stroke="#fff" stroke-width="1.2"/>
        </svg>
        <span class="contact-rule"></span>
        <span class="contact-text">Email: Darrel@Plankhorn.com</span>
      </li>
    </ul>
  </div>
</body>
</html>
```